Design to promote Vacation Tune Quest Series for Kids

We are a small local music school in need of a poster design to promote our new Vacation Tune Quest Series (sort of like a music camp) for the January 2013 Summer Break here in Sydney, Australia.

We generally teach students private instruments (e.g piano, guitar, bass, singing, drums, trumpet and theory) and offer group classes for Chorus Crew and Group Guitar.

The proposed Vacation Tune Quest Series goes for 1 week and is 'Jam Packed' with lots of fun musical activities, workshops and musical experiences.

It's called 'Turn Your Rhythm Loose' and is designed for Kids aged 7 - 12 yrs of age.

We would like an A3 size poster to be designed and an A6 size flyer which compliments the poster. If you're able to also resize the A3 size poster to A4 that'll be great. The successful candidate can do that once the final design is confirmed.

The look and feel should be 'Summer', fun, musical, hip and targeted at young parents aged 28 - 50yrs old. These parents are generally professionals living in a creative area of Sydney.

Text to be included as follows:

'TURN YOUR RHYTHM LOOSE'
A Fun Jam Packed Vacation Tune Quest Series for the Summer Break

Designed for Kids 7 - 12 years old

14 - 18 January, 2013
NEWTOWN

No experience necessary

INSTRUMENTAL DISCOVERY Learn and play a variety of musical instruments
SONG WRITING Write your own songs
BEAT BOXING Learn to beat box and rap
MUSIC GAMES Join in a number of fun musical games and activities
GLEE Do some singing (no problems if you've never tried)
MUSIC TECHNOLOGY Learn about music technology and how to record/produce songs
HAVE FUN!

EARLY BIRD REGISTRATION: $280 per child (when you enrol by 14 December, 2012)

COST: $300 per child
*discounts apply when enrolling 2 or more kids

Goes from Monday - Friday, 9:00am - 3:00pm

ENROL ONLINE NOW
www.brindlewavetunes.example
Or call 02 7412 5589 / 0432 987 654

For enquiries or more info visit our website or email info@brindlewavetunes.example

Brindlewave Music School
Unit 4B, 58 Corwen Street, Newtown (enter via Pellham Ave)

Target Market(s)

Parents of children aged 7 - 12 yrs. They would be around 25 - 50 yrs old

Industry/Entity Type

School

Requirements
Must have
• Must include our company logo - there are two versions which you can pick from to use.

```html
<!DOCTYPE html>
<html lang="en">
<head>
<meta charset="utf-8">
<title>Turn Your Rhythm Loose – Brindlewave Music School</title>
<link rel="stylesheet" href="https://fonts.googleapis.com/css2?family=Barlow:wght@500;600;700;800&family=Barlow+Condensed:wght@700;800&family=Bowlby+One&display=swap">
<style>
  :root {
    --orange: #e8561e;
    --orange-deep: #d24a16;
    --teal: #3aa9b9;
    --teal-light: #7ccbd6;
    --white: #ffffff;
    --photo-a: #9fd8c8;
    --photo-b: #f2a3c9;
    --photo-c: #ffd166;
  }
  * { box-sizing: border-box; margin: 0; padding: 0; }
  html, body { width: 849px; height: 1200px; overflow: hidden; background: var(--white); }
  .poster {
    position: relative; width: 849px; height: 1200px; overflow: hidden;
    background: var(--white); font-family: "Barlow", Arial, sans-serif;
  }
  .top-band { position: absolute; left: 0; top: 0; width: 100%; height: 42px; background: var(--teal-light); }
  .bottom-band { position: absolute; left: 0; bottom: 0; width: 100%; height: 208px; background: var(--teal); }

  .brand { position: absolute; left: 42px; top: 172px; display: flex; align-items: center; gap: 10px; }
  .brand-dot { width: 18px; height: 18px; border-radius: 50%; background: var(--teal); flex: none; }
  .brand-name { font-size: 24px; font-weight: 700; color: var(--teal); line-height: 1; white-space: nowrap; }

  .event-date {
    position: absolute; left: 40px; top: 238px;
    font-size: 37px; font-weight: 600; color: var(--orange); line-height: 1.05; text-transform: uppercase;
  }

  .hero-photo {
    position: absolute; left: 228px; top: 42px; width: 520px; height: 310px;
    background: linear-gradient(115deg, var(--photo-a) 0%, var(--photo-b) 50%, var(--photo-c) 100%);
    opacity: 0.75; border-radius: 4px;
  }

  .headline { position: absolute; left: 0; top: 330px; width: 849px; height: 300px; overflow: visible; }
  .headline text {
    font-family: "Bowlby One", Impact, sans-serif; fill: var(--orange);
    stroke: var(--white); stroke-width: 10px; paint-order: stroke; stroke-linejoin: round;
  }
  .headline .shade { fill: var(--orange-deep); stroke: none; opacity: 0.35; }

  .age-note {
    position: absolute; left: 666px; top: 520px;
    font-size: 20px; font-weight: 800; color: var(--teal);
    line-height: 1.05; text-transform: uppercase;
  }

  .tagline-ribbon { position: absolute; left: 100px; top: 632px; width: 670px; height: 100px; }
  .tagline-ribbon .ribbon { fill: var(--teal); }
  .tagline-ribbon text {
    font-family: "Barlow Condensed", Arial, sans-serif; font-weight: 800; font-size: 31px;
    fill: var(--white); letter-spacing: 1px; text-anchor: middle;
  }

  .info-panel {
    position: absolute; left: 40px; top: 743px; width: 768px; height: 348px;
    background: var(--orange); border: 3px solid var(--white); border-radius: 14px;
    color: var(--white);
  }
  .info-divider { position: absolute; left: 385px; top: 22px; height: 300px; border-left: 2px dotted rgba(255,255,255,0.8); }

  .activities { position: absolute; left: 22px; top: 16px; width: 350px; }
  .activities-title { font-size: 21px; font-weight: 700; text-transform: uppercase; margin-bottom: 4px; }
  .activity-name { font-size: 16px; font-weight: 800; text-transform: uppercase; line-height: 1.08; }
  .activity-desc { font-size: 16px; font-weight: 500; line-height: 1.1; }
  .activity-desc.narrow { width: 200px; }
  .activity-desc.mid { width: 240px; }
  .activity-desc.wide { width: 300px; }

  .kid-photo {
    position: absolute; left: 220px; top: 50px; width: 150px; height: 150px; border-radius: 50%;
    background: radial-gradient(circle at 50% 45%, #f0b27a 0%, #c2703c 55%, rgba(210,74,22,0) 75%);
  }

  .detail { position: absolute; left: 408px; width: 350px; }
  .detail.early { top: 22px; }
  .detail.cost { top: 104px; }
  .detail.schedule { top: 180px; }
  .detail.enrol { top: 254px; }
  .detail-head { font-size: 21px; font-weight: 800; text-transform: uppercase; line-height: 1.02; }
  .detail-text { font-size: 19px; font-weight: 500; text-transform: uppercase; line-height: 1.05; }
  .detail-small { font-size: 15px; font-weight: 600; text-transform: uppercase; line-height: 1.3; }
  .detail-text.cta-link { font-weight: 800; font-size: 19px; }
  .detail-text.cta-phone { text-transform: none; font-size: 19px; font-weight: 600; }
  .detail-text.cta-phone strong { font-weight: 800; }

  .footer {
    position: absolute; left: 0; top: 1110px; width: 100%; text-align: center;
    color: var(--white); font-size: 18px; font-weight: 600; line-height: 1.35;
  }
</style>
</head>
<body>
<main class="poster">
  <div class="top-band"></div>
  <div class="bottom-band"></div>

  <div class="hero-photo" role="img" aria-label="Photo of three girls in bright tutus singing into microphones and playing an electric guitar"></div>

  <header class="brand">
    <span class="brand-dot"></span>
    <p class="brand-name">Brindlewave Music</p>
  </header>

  <p class="event-date">14-18/ Jan<br>Newtown<br>2013</p>

  <svg class="headline" viewBox="0 0 849 300" aria-label="Turn Your Rhythm Loose">
    <g transform="rotate(-4 425 150)">
      <text class="shade" x="146" y="148" font-size="118" textLength="560" lengthAdjust="spacingAndGlyphs">TURN YOUR</text>
      <text x="140" y="140" font-size="118" textLength="560" lengthAdjust="spacingAndGlyphs">TURN YOUR</text>
      <text class="shade" x="84" y="278" font-size="112" textLength="560" lengthAdjust="spacingAndGlyphs">RHYTHM LOOSE</text>
      <text x="78" y="270" font-size="112" textLength="560" lengthAdjust="spacingAndGlyphs">RHYTHM LOOSE</text>
    </g>
  </svg>

  <p class="age-note">Designed<br>for kids<br>7 - 12 years<br>old</p>

  <svg class="tagline-ribbon" viewBox="0 0 670 100" aria-label="A fun jam packed vacation tune quest series for the summer break">
    <polygon class="ribbon" points="0,4 670,22 664,100 8,80"/>
    <g transform="rotate(1.6 335 50)">
      <text x="335" y="42">A FUN JAM PACKED VACATION TUNE QUEST</text>
      <text x="335" y="78">SERIES FOR THE SUMMER BREAK</text>
    </g>
  </svg>

  <section class="info-panel">
    <div class="info-divider"></div>
    <div class="kid-photo" role="img" aria-label="Photo of a young boy in a hat sitting cross-legged playing an acoustic guitar"></div>

    <div class="activities">
      <p class="activities-title">No experience necessary</p>
      <p class="activity-name">Instrumental discovery</p>
      <p class="activity-desc narrow">Learn and play a variety of musical instruments</p>
      <p class="activity-name">Song writing</p>
      <p class="activity-desc">&nbsp;Write your own songs</p>
      <p class="activity-name">Beat boxing</p>
      <p class="activity-desc">Learn to beat box and rap</p>
      <p class="activity-name">Music games</p>
      <p class="activity-desc mid">Join in a number of fun musical games and activities</p>
      <p class="activity-name">Glee</p>
      <p class="activity-desc wide">Do some singing (no problems if you've never tried)</p>
      <p class="activity-name">Music technology</p>
      <p class="activity-desc wide">Learn about music technology and how to record/produce songs</p>
    </div>

    <div class="detail early">
      <p class="detail-head">Early bird registration:<br>$280 per child</p>
      <p class="detail-small">&nbsp;(When you enrol by 14 December, 2012)</p>
    </div>
    <div class="detail cost">
      <p class="detail-head">Cost: $300 per child</p>
      <p class="detail-small">*Discounts apply when enrolling<br>&nbsp;2 or more kids</p>
    </div>
    <div class="detail schedule">
      <p class="detail-head">Goes from:</p>
      <p class="detail-text">Monday - Friday<br>9:00am - 3:00pm</p>
    </div>
    <div class="detail enrol">
      <p class="detail-head">Enrol online now:</p>
      <p class="detail-text cta-link">www.brindlewavetunes.example</p>
      <p class="detail-text cta-phone">Or call <strong>02 7412 5589 / 0432 987 654</strong></p>
    </div>
  </section>

  <footer class="footer">
    <p>For enquiries or more info visit our website or email info@brindlewavetunes.example</p>
    <p>Brindlewave Music School, Unit 4B, 58 Corwen Street, Newtown (enter via Pellham Ave)</p>
  </footer>
</main>
</body>
</html>
```